U.S. Popcorn company needs business cards

We are a popcorn company that manufactures popcorn and sells it to grocery stores worldwide. Our theme is "Americana" and our logo is Kettle Mesa Byway which is the most famous highway in the U.S.

We would like the design to be simple and to use both sides. On the back side we would like to see just the logo and website. The front would be normal details

Target Market(s)

Wholesalers, grocers and distributors

Industry/Entity Type

Manufacture

Contact Information for Business Card

Business name: Kettle Mesa Popcorn
Phone: +1 555 014 2286
Email: Dale@kettlemesapopcorn.com
website: www.kettlemesapopcorn.com
Tag Line: "Fresh from the kettle"
Name: Dale Whitcombe
Title: Founder/President

Requirements
Must have
• Either this design should be fun or clean and simple. I will let you show me your thougths.
Nice to have
• Anything that ties in the real Kettle Mesa Byway.
• Colors might need to be red, white and blue incorporated.
Should not have
• Not be too busy.

```html
<!DOCTYPE html>
<html lang="en">
<head>
<meta charset="utf-8">
<title>Kettle Mesa Popcorn – Business Cards</title>
<link href="https://fonts.googleapis.com/css2?family=PT+Sans:wght@400;700&family=Comic+Neue:wght@400;700&display=swap" rel="stylesheet">
<style>
  :root {
    --navy: #262262;
    --red: #ed1c24;
    --white: #ffffff;
    --backdrop: #5a4048;
    --shadow: rgba(0, 0, 0, 0.35);
  }
  html, body {
    margin: 0;
    padding: 0;
    width: 1200px;
    height: 1200px;
    overflow: hidden;
    background: var(--backdrop);
    font-family: "PT Sans", Arial, sans-serif;
  }
  .card {
    position: absolute;
    left: 239px;
    width: 722px;
    height: 409px;
    box-shadow: 0 4px 10px var(--shadow);
    overflow: hidden;
  }
  .card--front { top: 158px; background: var(--white); }
  .card--back { top: 634px; background: var(--navy); }

  .swoosh { position: absolute; left: 0; top: 0; width: 722px; height: 409px; }

  .brand {
    position: absolute;
    margin: 0;
    font-weight: 700;
    line-height: 1.05;
    text-align: center;
    display: flex;
    flex-direction: column;
    align-items: center;
    gap: 10px;
  }
  .brand__dot {
    width: 18px;
    height: 18px;
    border-radius: 50%;
    background: var(--red);
  }
  .card--front .brand {
    left: 50px;
    top: 92px;
    width: 240px;
    font-size: 34px;
    color: var(--navy);
  }
  .card--back .brand {
    left: 0;
    top: 124px;
    width: 722px;
    font-size: 44px;
    color: var(--white);
  }

  .divider {
    position: absolute;
    left: 318px;
    top: 54px;
    width: 2px;
    height: 300px;
    background: var(--red);
  }
  .details { position: absolute; left: 353px; top: 96px; }
  .person__name {
    margin: 0;
    font-size: 33px;
    line-height: 1;
    color: var(--red);
    font-weight: 400;
  }
  .person__name strong { font-weight: 700; }
  .person__title {
    margin: 4px 0 0;
    font-size: 21px;
    color: var(--navy);
  }
  .contact {
    list-style: none;
    margin: 36px 0 0;
    padding: 0;
  }
  .contact__item {
    display: flex;
    align-items: center;
    gap: 12px;
    height: 28px;
    font-size: 21px;
    color: var(--navy);
  }
  .contact__icon { width: 22px; height: 18px; flex: none; }
  .tagline {
    margin: 36px 0 0;
    font-family: "Comic Neue", "Comic Sans MS", cursive;
    font-weight: 700;
    font-size: 23px;
    color: var(--navy);
  }
  .tagline__lead { color: var(--red); }

  .back__web {
    position: absolute;
    left: 0;
    top: 332px;
    width: 722px;
    text-align: center;
    color: var(--white);
    font-size: 21px;
  }
</style>
</head>
<body>

<section class="card card--front">
  <svg class="swoosh" viewBox="0 0 722 409" aria-hidden="true">
    <path d="M0,146 Q70,330 214,409 L0,409 Z" fill="var(--navy)"/>
    <path d="M26,194 Q120,350 290,409 L228,409 Q100,350 26,194 Z" fill="var(--red)"/>
  </svg>

  <h1 class="brand">
    <span class="brand__dot"></span>
    <span>Kettle Mesa<br>Popcorn</span>
  </h1>

  <div class="divider"></div>

  <div class="details">
    <h2 class="person__name"><strong>Dale</strong> Whitcombe</h2>
    <p class="person__title">Founder/President</p>
    <ul class="contact">
      <li class="contact__item">
        <svg class="contact__icon" viewBox="0 0 22 18" aria-hidden="true">
          <path d="M1,6 Q11,-2 21,6 L18,8 L15,6 L15,4 Q11,2 7,4 L7,6 L4,8 Z" fill="var(--red)"/>
          <path d="M6,8 L16,8 L20,17 L2,17 Z" fill="var(--red)"/>
          <circle cx="11" cy="12.5" r="2.3" fill="var(--white)"/>
        </svg>
        +1 555 014 2286
      </li>
      <li class="contact__item">
        <svg class="contact__icon" viewBox="0 0 22 18" aria-hidden="true">
          <rect x="1" y="2" width="20" height="14" fill="var(--red)"/>
          <path d="M1,2 L11,10 L21,2 M1,16 L8,8 M21,16 L14,8" stroke="var(--white)" stroke-width="1.6" fill="none"/>
        </svg>
        Dale@kettlemesapopcorn.com
      </li>
      <li class="contact__item">
        <svg class="contact__icon" viewBox="0 0 22 18" aria-hidden="true">
          <g fill="none" stroke="var(--red)" stroke-width="1.4">
            <circle cx="11" cy="9" r="8"/>
            <ellipse cx="11" cy="9" rx="3.5" ry="8"/>
            <path d="M3,9 H19 M4.5,4.5 H17.5 M4.5,13.5 H17.5"/>
          </g>
        </svg>
        www.kettlemesapopcorn.com
      </li>
    </ul>
    <p class="tagline"><span class="tagline__lead">Fresh</span> from the kettle</p>
  </div>
</section>

<section class="card card--back">
  <h2 class="brand">
    <span class="brand__dot"></span>
    <span>Kettle Mesa<br>Popcorn</span>
  </h2>
  <p class="back__web">www.kettlemesapopcorn.com</p>
</section>

</body>
</html>
```